KTR Business Card

We need a new design for our business cards. We are brokers in the scrap metal industry and wants something nice, clean and very professional.

Industry/Entity Type

Business

Requirements
Must have
• Our logo
• Would probably be good to incorporate colors from logo into design.
• Example info we need on the cards.
• Name
• Company Address
• Cell Phone
• Office Phone
• Fax
• Email
• Company Website
Should not have
• Should not be too cluttered. Needs to be nice, clean and professional looking.

```html
<!DOCTYPE html>
<html lang="en">
<head>
<meta charset="utf-8">
<title>KTR Business Card</title>
<link href="https://fonts.googleapis.com/css2?family=PT+Sans:wght@400;700&family=PT+Sans+Narrow:wght@700&display=swap" rel="stylesheet">
<style>
  :root {
    --navy-deep: #05305e;
    --navy-mid: #0a4f86;
    --blue-light: #0a6498;
    --ink-dark: #1f1f1f;
    --paper: #ffffff;
    --stage: #e9e7e3;
    --accent-navy: #0b2a52;
  }
  * { margin: 0; padding: 0; box-sizing: border-box; }
  html, body { width: 1200px; height: 1000px; overflow: hidden; }
  body {
    position: relative;
    background: var(--stage);
    font-family: "PT Sans", sans-serif;
    color: var(--paper);
  }
  .card {
    position: absolute;
    box-shadow: 0 2px 6px rgba(0,0,0,0.25);
    overflow: hidden;
  }
  /* Front side */
  .card-front {
    left: 18px; top: 32px; width: 744px; height: 478px;
    background: linear-gradient(to bottom, var(--navy-deep), var(--blue-light));
  }
  .front-mark {
    position: absolute; left: 336px; top: 140px;
    width: 136px; height: 136px;
    background: var(--paper);
  }
  .front-name {
    position: absolute; left: 0; right: 0; top: 296px;
    text-align: center;
    font-family: "PT Sans Narrow", sans-serif;
    font-weight: 700; font-size: 38px; letter-spacing: -0.3px;
    color: var(--paper);
  }
  .front-web {
    position: absolute; left: 0; right: 0; top: 428px;
    text-align: center;
    font-family: "PT Sans Narrow", sans-serif;
    font-weight: 700; font-size: 23px;
  }
  .front-web .domain { color: var(--accent-navy); }
  /* Back side */
  .card-back {
    left: 435px; top: 500px; width: 736px; height: 472px;
    display: flex;
  }
  .brand-panel {
    position: relative;
    width: 265px; height: 100%;
    background: var(--paper);
  }
  .brand-mark {
    position: absolute; left: 82px; top: 128px;
    width: 100px; height: 100px;
    background: var(--navy-mid);
  }
  .brand-name {
    position: absolute; left: 0; right: 0; top: 252px;
    text-align: center;
    font-family: "PT Sans Narrow", sans-serif;
    font-weight: 700; font-size: 26px; letter-spacing: -0.3px;
    color: var(--ink-dark);
  }
  .info-panel {
    position: relative;
    flex: 1;
    background: linear-gradient(to bottom, var(--blue-light), var(--navy-deep));
  }
  .person-name {
    position: absolute; left: 0; right: 0; top: 74px;
    text-align: center; font-weight: 700; font-size: 27px;
  }
  .person-title {
    position: absolute; left: 0; right: 0; top: 107px;
    text-align: center; font-size: 19px;
  }
  .contact-row {
    position: absolute; display: flex; font-size: 20px; line-height: 23px;
  }
  .contact-row dt {
    font-weight: 700; text-align: right; margin-right: 8px;
  }
  .details dt { width: 175px; }
  .details { left: 0; }
  .row-address { top: 216px; }
  .row-phone { top: 269px; }
  .row-fax { top: 299px; }
  .online dt { width: 80px; margin-right: 12px; }
  .online { left: 0; }
  .row-email { top: 405px; }
  .row-web { top: 434px; }
</style>
</head>
<body>
  <section class="card card-front" aria-label="Card front">
    <div class="front-mark"></div>
    <div class="front-name">Kestrel Trade Resources</div>
    <div class="front-web">Web: www.<span class="domain">kestreltraderesources</span>.com</div>
  </section>

  <section class="card card-back" aria-label="Card back">
    <div class="brand-panel">
      <div class="brand-mark"></div>
      <div class="brand-name">Kestrel Trade Resources</div>
    </div>
    <div class="info-panel">
      <div class="person-name">YOUR NAME</div>
      <div class="person-title">TITLE</div>

      <dl class="contact-row details row-address"><dt>Address:</dt><dd>1257 Harbor Loop West<br>Columbia,SC 29160</dd></dl>
      <dl class="contact-row details row-phone"><dt>Telephone:</dt><dd>(555) 210-4388</dd></dl>
      <dl class="contact-row details row-fax"><dt>Fax:</dt><dd>(555) 210-4377</dd></dl>

      <dl class="contact-row online row-email"><dt>Email:</dt><dd>info@kestreltraderesources.com</dd></dl>
      <dl class="contact-row online row-web"><dt>Web:</dt><dd>www.kestreltraderesources.com</dd></dl>
    </div>
  </section>
</body>
</html>
```